Body Wash & Shampoo Label Design

Hello everyone,

I need a new logo/label design for a sister line of products to our main line. The Brand name is Bramble Trailway.

Here’s some insight to provide some inspiration. This brand will be social media based and will focus on adventure, travel, hiking, camping, and all other outdoors activities. Target market is outdoorsman – women. We will also be allocating a percentage of sales to various conservation efforts which we are narrowing down as we speak.

I’m not exactly sure what we are looking for in a logo/label designs so we are open to ideas and promote creativity. That said, we are looking for a simple and clean design that also speaks to our target market and would like the logo & label to be done at the same time so they compliment each other and fit well together.

Please incorporate an accent color somewhere in the design so new fragrances can be added down the line. This label will be going on a 16 fl oz cylindrical bottle with a toggle cap.

Label Details:

Width: 7.4 in
Height: 5.5 in
Distance from center of front to center of back: 3.7 in

Front (left):
- Logo
- Product Name: Rinse Free Shampoo & Body Cleanser
- Highlights:
o No Rinse Nourishing Formula
o Sooths & Conditions
o Non-Sensitizing
o Non-Allergenic
- 16 Fl. Oz.

Back (right):

Tagline: More Cleanse, Less Hassle

Directions: Moisten wash cloth with Rinse Free Shampoo & body cleanser. Use wash cloth to gently cleanse desired area. Pat dry if necessary. When shampooing, use was cloth to gently massage hair and scalp. Let air dry.

Warning: For external use only. Rinse eyes with water if contact should occur. Discontinue use in the case of local irritation. Contact physician if irritation persists for extended period of time.

Ingredients: Water, Disodium Cocoamphodiactate, Sodium C14-16 Olefine Sulfonate, ppg-2 hydroxyethyl Cocamide, Styrene/Acrylates Copolymer, Germaben II, Acrylates/C10-30 Alkyl Acrylate Crosspolymer, Fragrance, Aloe Barbadeniss Leaf Juice

Made in USA (either logo or words)

Address:
Halvern Products
214 Larch Ave
Wexley, NJ 07456

Barcode is also attached below. Looking forward to seeing your designs and thanks for the help! Let me know if you have any questions.

- Glen

Target Market(s)

Outdoorsman/women

Logo Text

Bramble Trailway

Colors

Designer to choose colors to be used in the design.

```html
<!DOCTYPE html>
<html lang="en">
<head>
<meta charset="utf-8">
<title>Bramble Trailway – Rinse Free Shampoo &amp; Body Cleanser Label</title>
<link rel="stylesheet" href="https://fonts.googleapis.com/css2?family=Great+Vibes&family=Josefin+Sans:wght@400&family=Roboto+Condensed:ital,wght@0,700;1,400&display=swap">
<style>
  :root {
    --backdrop: #f3f3f3;
    --mint-top: #8fd0b6;
    --mint-mid: #c4e7d9;
    --label-white: #ffffff;
    --brand-green: #2c8a6c;
    --script-green: #2f8f6e;
    --ink: #1f2a27;
    --accent-teal: #2bb39a;
    --accent-deep: #1c7a8c;
  }
  * { margin: 0; padding: 0; box-sizing: border-box; }
  html, body {
    width: 1200px; height: 900px; overflow: hidden;
    background: var(--backdrop);
  }
  .canvas { position: relative; width: 1200px; height: 900px; }

  .label-front {
    position: absolute;
    left: 468px; top: 114px;
    width: 264px; height: 732px;
    border-radius: 8px;
    background: linear-gradient(180deg,
      var(--mint-top) 0%,
      var(--mint-mid) 26%,
      var(--label-white) 46%,
      var(--label-white) 80%,
      #eef7f3 100%);
    color: var(--ink);
  }

  .brand-name {
    position: absolute; left: 0; right: 0; top: 208px;
    font-family: "Josefin Sans", sans-serif;
    font-weight: 400;
    font-size: 24px;
    letter-spacing: 1px;
    line-height: 1.15;
    text-transform: uppercase;
    text-align: center;
    color: var(--brand-green);
  }

  .product-title {
    font-family: "Great Vibes", cursive;
    font-weight: 400;
    font-size: 62px;
    line-height: 1;
    color: var(--script-green);
  }
  .product-title .word { position: absolute; white-space: nowrap; }
  .product-title .word-first { left: 16px; top: 268px; }
  .product-title .word-second { left: 108px; top: 300px; }

  .product-type {
    position: absolute; left: 128px; top: 394px;
    font-family: "Roboto Condensed", sans-serif;
    font-style: italic;
    font-size: 18px;
    line-height: 1.2;
    color: var(--ink);
  }

  .accent-artwork {
    position: absolute; left: 18px; top: 440px;
    width: 222px; height: 126px;
  }

  .highlights {
    position: absolute; left: 0; right: 0; top: 584px;
    list-style: none;
    font-family: "Roboto Condensed", sans-serif;
    font-style: italic;
    font-size: 11.5px;
    line-height: 15px;
    text-align: center;
    color: var(--ink);
  }

  .net-volume {
    position: absolute; left: 0; right: 0; top: 650px;
    font-family: "Roboto Condensed", sans-serif;
    font-weight: 700;
    font-size: 19px;
    text-align: center;
    color: var(--ink);
  }
</style>
</head>
<body>
<main class="canvas">
  <section class="label-front">
    <div class="brand-name">Bramble<br>Trailway</div>

    <h1 class="product-title">
      <span class="word word-first">Rinse</span>
      <span class="word word-second">free</span>
    </h1>

    <p class="product-type">Shampoo &amp;<br>Body Cleanser</p>

    <svg class="accent-artwork" viewBox="0 0 222 126" role="img" aria-label="Accent artwork: fanned green and teal feather-like swoosh">
      <defs>
        <radialGradient id="accentGlow" cx="58%" cy="55%" r="55%">
          <stop offset="0%" stop-color="var(--accent-deep)" stop-opacity="0.85"/>
          <stop offset="45%" stop-color="var(--accent-teal)" stop-opacity="0.5"/>
          <stop offset="100%" stop-color="var(--accent-teal)" stop-opacity="0"/>
        </radialGradient>
      </defs>
      <ellipse cx="116" cy="66" rx="106" ry="58" fill="url(#accentGlow)"/>
    </svg>

    <ul class="highlights">
      <li>No Rinse Nourishing Formula</li>
      <li>Sooths &amp; Conditions</li>
      <li>Non-Sensitizing</li>
      <li>Non-Allergenic</li>
    </ul>

    <div class="net-volume">16 Fl. Oz</div>
  </section>
</main>
</body>
</html>
```